Billboard design for a jewelry store.

I am looking for a very unique design with a catchy slogan, I am looking for billboard so good that will make the front page of the newspaper. I want to target customers that are looking for diamond jewelry or diamonds in general. For sure not interested in anything that is genetic or been used in the past. I want the billboard to stand out and very unique. Text not more than 3 words, our logo and an image.

Target Market(s)

Local

Industry/Entity Type

Jewelry Store

Font styles to use
Other font styles liked:
• Open to your suggestion for the font.

Requirements
Must have
• Unique, very brief a catchy slogan. My logo and an image. Open for suggestions. I want also different formats to use on social media.
Nice to have
• I am open to unique and amazing new ideas. I don't want general used design or slogan.
Should not have
• Too much text

```html
<!DOCTYPE html>
<html lang="en">
<head>
<meta charset="utf-8">
<title>Vellor Jewelers – Ultimate Luxury &amp; Style Billboard</title>
<link rel="stylesheet" href="https://fonts.googleapis.com/css2?family=Dancing+Script:wght@400&display=swap">
<style>
  :root {
    --frame-grey: #d1d2d4;
    --panel-black: #050505;
    --text-white: #ffffff;
    --rock-deep: #151516;
    --rock-dark: #242426;
    --rock-mid: #3c3c3f;
    --rock-light: #55565a;
    --gem-shadow: #6e7280;
    --gem-light: #b9bdcb;
    --gem-bright: #eceef5;
  }
  * { margin: 0; padding: 0; box-sizing: border-box; }
  html, body {
    width: 1200px;
    height: 478px;
    overflow: hidden;
    background: var(--frame-grey);
  }
  .billboard {
    position: relative;
    width: 1200px;
    height: 478px;
    background: var(--frame-grey);
  }
  .billboard-panel {
    position: absolute;
    left: 50px;
    top: 54px;
    width: 1100px;
    height: 370px;
    background: var(--panel-black);
    overflow: hidden;
  }
  .hero-photo {
    position: absolute;
    left: 0;
    top: 0;
    width: 560px;
    height: 370px;
    background:
      radial-gradient(ellipse 165px 125px at 205px 170px,
        var(--gem-bright) 0%, var(--gem-light) 45%, var(--gem-shadow) 72%, rgba(70,72,80,0) 100%),
      radial-gradient(ellipse 130px 90px at 330px 200px,
        rgba(210,214,228,0.55) 0%, rgba(210,214,228,0) 100%),
      radial-gradient(ellipse 360px 260px at 330px 300px,
        var(--rock-light) 0%, var(--rock-mid) 35%, var(--rock-dark) 70%, rgba(20,20,22,0) 100%),
      radial-gradient(ellipse 300px 200px at 90px 70px,
        var(--rock-mid) 0%, var(--rock-dark) 60%, rgba(20,20,22,0) 100%),
      linear-gradient(100deg, var(--rock-dark) 0%, var(--rock-deep) 70%, var(--panel-black) 100%);
  }
  .slogan {
    position: absolute;
    left: 566px;
    top: 50px;
    width: 500px;
    text-align: center;
    color: var(--text-white);
    font-family: "Dancing Script", cursive;
    font-weight: 400;
    font-size: 74px;
    line-height: 72px;
  }
  .brand-name {
    position: absolute;
    left: 616px;
    top: 272px;
    width: 400px;
    text-align: center;
    color: var(--text-white);
    font-family: "Dancing Script", cursive;
    font-weight: 400;
    font-size: 36px;
    line-height: 42px;
  }
</style>
</head>
<body>
  <div class="billboard">
    <div class="billboard-panel">
      <div class="hero-photo" role="img" aria-label="Photograph of a large brilliant-cut diamond lying on its side on a dark rough stone"></div>
      <h1 class="slogan">Ultimate<br>Luxury &amp; Style</h1>
      <p class="brand-name">Vellor Jewelers</p>
    </div>
  </div>
</body>
</html>
```